Jetzt starten So funktioniert'sAuf die Visitenkarte soll ein Logo bzw. eine Grafik dargestellt werden, welche ebenfalls auf der Website und dem Flyer genutzt werden soll wird es hier als Logo bezeichnet. Die Grafik soll ein Labyrinth und eine Person in einer scheinbar aussichtsloser Lage darstellen mit der Frage „WANDEL gefä..
16Stein, Weg, Füße, Baby o. Kind....Sonne... Vielleicht fällt Ihnen auch etwas besseres ein. Evtl. ein Slogan wie z. B. -Kinderbetreuung mit ❤️ - Hier steht das Kind im Mittelpunkt. -Jedes Kind ist einzigartig? Oder - „Hilf mir es selbst zu tun“ aber vielleicht anders formuliert. (..
40Es müssen für zwei Geschäfte Visitenkarten, Briefpapier (A4) und Kassenkassenbelege (A6) erstellt werden. Logo und Typo im Anhang. Ein Farbkonzept besteht noch nicht. Die Idee geht in Richtung Bordeaux-Rot. Generell: (1) Sieht erstmal nach viel Beschreibung aus, bitte nicht entmutigen lass..
118Schlichtes aber direkt erkennbares Design. Koch dir Kraft , Gesundheit und Ernährungsberatung ( gut lesbar , elegant) Marlene Obrist-Kähler ( nicht so groß ) Grau ; Grün Töne und gerne etwas rosa Infos wie Adresse und E-Mail vielleicht in jeweilige Blöcke am unteren Rand
30Wir benötigen, passend zu unserem neuen Logo, Geschäftspapier, Visitenkarten und eine Vorlage für eine PowerPoint Präsentation (Hintergrunds-Seite)

```html
<!DOCTYPE html>
<html lang="de">
<head>
<meta charset="utf-8">
<title>Jonas Veldmann – Geschäftsausstattung</title>
<link rel="stylesheet" href="https://fonts.googleapis.com/css2?family=Crimson+Text:wght@400;600&display=swap">
<style>
  :root {
    --blue: #3b4d9e;
    --tan: #b8977a;
    --ink: #7a4a2c;
    --paper: #ffffff;
    --backdrop: #eceef1;
    --serif: "Crimson Text", "Times New Roman", serif;
  }
  * { margin: 0; padding: 0; box-sizing: border-box; }
  html, body { width: 922px; height: 1200px; overflow: hidden; }
  body { background: var(--backdrop); font-family: var(--serif); position: relative; }

  .letterhead {
    position: absolute; left: 30px; top: 40px;
    width: 700px; height: 990px;
    background: var(--paper);
    box-shadow: 0 0 0 1px #d6d8dc;
    overflow: hidden;
  }
  .block { position: absolute; }
  .blue { background: var(--blue); }
  .tan { background: var(--tan); }

  .brand-name {
    position: absolute;
    color: #fff;
    font-weight: 400;
    text-transform: uppercase;
    white-space: nowrap;
    letter-spacing: 0.04em;
    line-height: 1;
  }
  .tagline {
    position: absolute;
    color: #fff;
    white-space: nowrap;
  }

  .letterhead .brand-name { right: 18px; top: 54px; font-size: 29px; }
  .letterhead .tagline { right: 18px; top: 102px; font-size: 13.5px; }

  .sender-line {
    position: absolute; left: 70px; top: 188px;
    font-size: 10px; color: var(--ink);
  }

  .footer-text {
    position: absolute; left: 70px; top: 898px;
    font-size: 10px; line-height: 15px; color: #5a4636;
  }
  .footer-text .contact { color: var(--ink); font-weight: 600; margin-bottom: 3px; }

  .business-card {
    position: absolute; left: 560px; top: 880px;
    width: 340px; height: 210px;
    background: var(--paper);
    box-shadow: 0 0 0 1px #d6d8dc;
    overflow: hidden;
  }
  .business-card .brand-name { right: 14px; top: 46px; font-size: 22px; }
  .business-card .tagline { right: 14px; top: 84px; font-size: 11px; }
  .card-address {
    position: absolute; left: 22px; top: 118px;
    font-size: 10.5px; line-height: 14px; color: var(--ink);
  }
</style>
</head>
<body>

<section class="letterhead" aria-label="Briefbogen">
  <div class="block blue" style="left:0;top:0;width:578px;height:90px"></div>
  <div class="block tan" style="left:578px;top:0;width:122px;height:51px"></div>
  <div class="block blue" style="left:578px;top:51px;width:122px;height:39px"></div>
  <div class="block tan" style="left:0;top:90px;width:700px;height:44px"></div>
  <div class="brand-name">Jonas Veldmann</div>
  <div class="tagline">Korrektorat • Textredaktion • Ghostwriting</div>

  <p class="sender-line">Jonas Veldmann Birkenhang 14, 24103 Hollerstedt</p>

  <div class="block tan" style="left:0;top:889px;width:578px;height:87px"></div>
  <div class="block blue" style="left:578px;top:889px;width:122px;height:101px"></div>
  <div class="block blue" style="left:0;top:976px;width:700px;height:14px"></div>
  <div class="footer-text">
    <p class="contact">Jonas Veldmann Birkenhang 14, 24103 Hollerstedt Tel. (0 43 21) 6 72 40 18 • j.veldmann@textpost.de</p>
    <p>Kto.-Nr. 41 276 300, Raiffkasse Hollerstedt eG, BLZ 210 508 17</p>
    <p>IBAN DE47210508170041276300, BIC GENODEF1HLS</p>
    <p>USt-IdNr. DE318204693</p>
  </div>
</section>

<section class="business-card" aria-label="Visitenkarte">
  <div class="block blue" style="left:0;top:0;width:230px;height:76px"></div>
  <div class="block tan" style="left:230px;top:0;width:110px;height:38px"></div>
  <div class="block blue" style="left:230px;top:38px;width:110px;height:38px"></div>
  <div class="block tan" style="left:0;top:76px;width:340px;height:26px"></div>
  <div class="brand-name">Jonas Veldmann</div>
  <div class="tagline">Korrektorat • Textredaktion • Ghostwriting</div>
  <div class="card-address">
    <p>Birkenhang 14, 24103 Hollerstedt</p>
    <p>Tel. (0 43 21) 6 72 40 18 • j.veldmann@textpost.de</p>
  </div>
  <div class="block tan" style="left:0;top:178px;width:230px;height:32px"></div>
  <div class="block blue" style="left:230px;top:160px;width:110px;height:50px"></div>
</section>

</body>
</html>
```